I need a business Card Design for my practice , i am clinical herbalist. I am a herbalist specializing in Lyme disease, autism, autoimmune diseases, difficult to cure diseasesDifficult to cure diseases. In my innovative practice i link traditional medicine, herbs with science, immunologu ,pharmacology.

Industry/Entity Type

Business

Contact Information for Business Card

My company name : OŚRODEK ZIELNIK
My name : Piotr Kaleta
Name of my profession : Fitoterapeuta
In Polish language Fitoterapeuta is Herbalist .

e-mail: piotrkaleta@osrodekzielnik.com
www.osrodek-zielnik.pl
phone : 604 587 231
My company adress : Dąbrowa Sitnicka 41 , 38-415 Modrzewiec
I dont have logo .

Requirements
Nice to have
• My company

```html
<!DOCTYPE html>
<html lang="pl">
<head>
<meta charset="utf-8">
<title>Ośrodek Zielnik – wizytówka</title>
<link rel="stylesheet" href="https://fonts.googleapis.com/css2?family=Roboto+Slab:wght@700;800&family=Open+Sans:wght@400;500&display=swap">
<style>
  :root {
    --backdrop: #565252;
    --card-white: #ffffff;
    --card-shade: #eef0ef;
    --brand-green: #6aac35;
    --ink: #1d1d1d;
    --rule-green: #9fcb7c;
    --rule-grey: #d6d6d6;
  }
  * { margin: 0; padding: 0; box-sizing: border-box; }
  html, body {
    width: 1200px; height: 1200px; overflow: hidden;
    background: var(--backdrop);
  }
  .stage {
    width: 1200px; height: 1200px;
    display: flex; align-items: center; justify-content: center;
  }
  .business-card {
    position: relative;
    width: 1000px; height: 572px;
    display: flex;
    background: linear-gradient(135deg, var(--card-white) 0%, var(--card-white) 45%, var(--card-shade) 100%);
    box-shadow: 0 10px 28px rgba(0,0,0,0.35);
    overflow: hidden;
  }
  .brand-band {
    width: 290px; height: 100%;
    flex-shrink: 0;
    background: var(--brand-green);
    display: flex; flex-direction: column;
    align-items: center; justify-content: center;
    gap: 22px;
  }
  .brand-band__circle {
    width: 150px; height: 150px;
    border: 3px solid var(--card-white);
    border-radius: 50%;
  }
  .brand-band__name {
    font-family: "Roboto Slab", serif;
    font-weight: 700;
    font-size: 22px;
    letter-spacing: 0.5px;
    color: var(--card-white);
  }
  .card-content {
    flex: 1;
    padding: 96px 60px 0 52px;
  }
  .company-name {
    font-family: "Roboto Slab", serif;
    font-weight: 800;
    font-size: 54px;
    line-height: 1;
    color: var(--brand-green);
    letter-spacing: 0.5px;
    white-space: nowrap;
  }
  .rule {
    height: 1px;
    background: var(--rule-green);
    margin: 18px 0 14px 0;
  }
  .person-name {
    font-family: "Open Sans", sans-serif;
    font-weight: 400;
    font-size: 40px;
    line-height: 1.1;
    color: var(--ink);
    white-space: nowrap;
  }
  .rule--grey {
    background: var(--rule-grey);
    margin: 20px 0 26px 0;
    width: 78%;
  }
  .contact-list { list-style: none; }
  .contact-list__item {
    display: flex; align-items: center; gap: 12px;
    font-family: "Open Sans", sans-serif;
    font-size: 22px;
    color: var(--ink);
    line-height: 1;
    margin-bottom: 16px;
    white-space: nowrap;
  }
  .contact-list__icon {
    width: 24px; height: 24px;
    display: flex; align-items: center; justify-content: center;
    font-weight: 500; font-size: 22px;
    flex-shrink: 0;
  }
  .contact-list__icon svg { width: 22px; height: 22px; fill: var(--ink); }
</style>
</head>
<body>
<main class="stage">
  <article class="business-card">
    <aside class="brand-band">
      <div class="brand-band__circle"></div>
      <span class="brand-band__name">OŚRODEK ZIELNIK</span>
    </aside>
    <section class="card-content">
      <h1 class="company-name">OŚRODEK ZIELNIK</h1>
      <div class="rule"></div>
      <p class="person-name">Piotr Kaleta (Fitoterapeuta)</p>
      <div class="rule rule--grey"></div>
      <ul class="contact-list">
        <li class="contact-list__item">
          <span class="contact-list__icon">
            <svg viewBox="0 0 24 24"><path d="M2 5h20v14H2z M3.5 6.5 12 13l8.5-6.5" fill="none" stroke="#1d1d1d" stroke-width="2"/><path d="M2 5h20L12 12.5z"/></svg>
          </span>
          <span>: piotrkaleta@osrodekzielnik.com</span>
        </li>
        <li class="contact-list__item">
          <span class="contact-list__icon">@</span>
          <span>: www.osrodek-zielnik.pl</span>
        </li>
        <li class="contact-list__item">
          <span class="contact-list__icon">
            <svg viewBox="0 0 24 24"><path d="M6.6 10.8c1.4 2.8 3.8 5.1 6.6 6.6l2.2-2.2c.3-.3.7-.4 1-.2 1.1.4 2.3.6 3.6.6.6 0 1 .4 1 1V20c0 .6-.4 1-1 1C10.6 21 3 13.4 3 4c0-.6.4-1 1-1h3.5c.6 0 1 .4 1 1 0 1.3.2 2.5.6 3.6.1.3 0 .7-.2 1z"/></svg>
          </span>
          <span>: 604 587 231</span>
        </li>
        <li class="contact-list__item">
          <span class="contact-list__icon">
            <svg viewBox="0 0 24 24"><path d="M9 3h6a2 2 0 0 1 2 2v2h4a1 1 0 0 1 1 1v11a1 1 0 0 1-1 1H3a1 1 0 0 1-1-1V8a1 1 0 0 1 1-1h4V5a2 2 0 0 1 2-2zm0 2v2h6V5z"/></svg>
          </span>
          <span>: Dąbrowa Sitnicka 41 , 38-415 Modrzewiec</span>
        </li>
      </ul>
    </section>
  </article>
</main>
</body>
</html>
```